Business Card Design Project

We are a construction company in Orange County, CA. We need a two sided business card. We would like the back to be our logo with web URL. Front should included Name, title, address, phone, fax and email address.

our address is
627 West Marrow Blvd, Suite 305
Fullerton, CA 92831

Our logo files are attached.

Construction

```html
<!DOCTYPE html>
<html lang="en">
<head>
<meta charset="utf-8">
<title>Strata Business Card</title>
<link href="https://fonts.googleapis.com/css2?family=Arimo:wght@400;700&display=swap" rel="stylesheet">
<style>
  :root {
    --page: #e9eaec;
    --paper: #ffffff;
    --brand-blue: #1f5d97;
    --deep-blue: #14477e;
    --sky-blue: #2f8fc0;
    --band-light: #3a93bd;
    --ink-white: #ffffff;
    --soft-white: rgba(255,255,255,0.85);
  }
  * { box-sizing: border-box; margin: 0; padding: 0; }
  html, body { width: 1200px; height: 902px; overflow: hidden; }
  body {
    background: var(--page);
    font-family: "Arimo", Arial, sans-serif;
    display: flex;
    align-items: center;
    justify-content: center;
    gap: 40px;
  }
  .card {
    width: 540px;
    height: 310px;
    border-radius: 18px;
    overflow: hidden;
    position: relative;
    box-shadow: 0 10px 28px rgba(0,0,0,0.18);
  }

  /* Logo side */
  .card-back { background: var(--paper); display: flex; flex-direction: column; }
  .card-back .logo-area {
    flex: 1;
    display: flex;
    align-items: center;
    justify-content: center;
  }
  .wordmark {
    font-weight: 700;
    color: var(--brand-blue);
    letter-spacing: 2px;
    line-height: 1;
  }
  .card-back .wordmark { font-size: 78px; }
  .url-band {
    height: 58px;
    background: linear-gradient(90deg, var(--band-light), var(--deep-blue));
    color: var(--ink-white);
    display: flex;
    align-items: center;
    justify-content: flex-end;
    padding-right: 34px;
    font-size: 20px;
    letter-spacing: 1px;
  }

  /* Details side */
  .card-front {
    background: linear-gradient(135deg, var(--sky-blue) 0%, #1f6aa5 45%, var(--deep-blue) 100%);
    color: var(--ink-white);
    display: flex;
    align-items: center;
  }
  .card-front .logo-block {
    width: 210px;
    display: flex;
    justify-content: center;
  }
  .card-front .wordmark { color: var(--ink-white); font-size: 38px; }
  .divider { width: 1px; height: 180px; background: var(--soft-white); }
  .details { padding-left: 28px; }
  .person-name { font-size: 18px; font-weight: 700; letter-spacing: 0.5px; }
  .person-title { font-size: 14px; margin-top: 3px; }
  .address { font-size: 12.5px; line-height: 1.5; margin-top: 16px; }
  .contacts { list-style: none; margin-top: 14px; font-size: 12.5px; line-height: 1.65; }
  .contacts li { display: flex; align-items: center; gap: 8px; }
  .contacts svg { width: 12px; height: 12px; flex: none; }
  .contacts .gap-before { margin-top: 8px; }
</style>
</head>
<body>
  <section class="card card-back" aria-label="Card back">
    <div class="logo-area">
      <div class="wordmark">STRATA</div>
    </div>
    <div class="url-band">www.stratabuild.com</div>
  </section>

  <section class="card card-front" aria-label="Card front">
    <div class="logo-block">
      <div class="wordmark">STRATA</div>
    </div>
    <div class="divider"></div>
    <div class="details">
      <p class="person-name">DALE MORROW</p>
      <p class="person-title">President</p>
      <p class="address">627 West Marrow Blvd, Suite 305<br>Fullerton, CA 92831</p>
      <ul class="contacts">
        <li>
          <svg viewBox="0 0 12 12"><path d="M3 1 L5 3.5 L4 5 Q5.5 7 7 8 L8.5 7 L11 9 L10 11 Q5 11 1 3 Z" fill="#fff"/></svg>
          714.555.0142
        </li>
        <li>
          <svg viewBox="0 0 12 12"><rect x="1" y="4" width="10" height="6" rx="1" fill="#fff"/><rect x="3" y="1" width="6" height="4" fill="#fff"/></svg>
          714.555.0187
        </li>
        <li class="gap-before">
          <svg viewBox="0 0 12 12"><rect x="1" y="2.5" width="10" height="7" rx="1" fill="#fff"/><path d="M1.5 3 L6 6.5 L10.5 3" stroke="#1f6aa5" fill="none"/></svg>
          dalemorrow@stratabuild.com
        </li>
        <li>
          <svg viewBox="0 0 12 12"><circle cx="6" cy="6" r="5" fill="none" stroke="#fff"/><ellipse cx="6" cy="6" rx="2" ry="5" fill="none" stroke="#fff"/><line x1="1" y1="6" x2="11" y2="6" stroke="#fff"/></svg>
          www.stratabuild.com
        </li>
      </ul>
    </div>
  </section>
</body>
</html>
```